3rd Annual Maple & Clover Fundraiser

This is our 3rd Annual Maple & Clover Dog Wash Extravagana to support Circle of Harlow Ridge Pet Center. Please see the attached flyer for the 2nd Annual. We loved this flyer! Please revamp with our logo attached and the new content provided. Let's keep to the same colors as the 2nd Annual flyer-no change. Date: Saturday April 25th 2020 10A-1PM. Rain Date: May 2nd. Same address as 2nd Annual.

Other font styles liked:
• See 2nd Annual Flyer

Colors
add136
e34297
6b449b

Requirements
Must have
• See attached 2nd annual flyer including colors
Nice to have

```html
<!DOCTYPE html>
<html lang="en">
<head>
<meta charset="utf-8">
<title>3rd Annual Maple &amp; Clover Dog Wash Extravagana</title>
<link href="https://fonts.googleapis.com/css2?family=Luckiest+Guy&family=Arimo:wght@400;700&display=swap" rel="stylesheet">
<style>
:root{
  --green:#add136;
  --pink:#db3a64;
  --purple:#8a68ae;
  --ink:#111;
  --paper:#fff;
  --backdrop:#2a2a2a;
  --display:"Luckiest Guy", Impact, "Arial Black", sans-serif;
  --body:"Arimo", Arial, sans-serif;
}
*{margin:0;padding:0;box-sizing:border-box}
html,body{width:1200px;height:816px;overflow:hidden;background:var(--backdrop)}
.canvas{position:relative;width:1200px;height:816px}
.flyer{position:absolute;left:320px;top:20px;width:560px;height:776px;background:var(--paper);overflow:hidden}
.shapes{position:absolute;inset:0}
.txt{position:absolute;white-space:nowrap;line-height:1}
.display{font-family:var(--display);font-weight:400;letter-spacing:0}
.body{font-family:var(--body);color:var(--ink)}
.annual{left:28px;top:62px;color:var(--paper);font-size:42px;line-height:46px;transform:rotate(-3deg);transform-origin:left top}
.brand{left:276px;top:108px;display:flex;align-items:center;gap:8px}
.brand-dot{width:16px;height:16px;border-radius:50%;background:var(--green)}
.brand-name{font-family:var(--display);font-size:28px;color:var(--purple)}
.title-1{left:0;width:680px;text-align:center;top:230px;font-size:25px}
.title-2{left:0;width:676px;text-align:center;top:267px;font-size:25px;color:var(--pink)}
.c-purple{color:var(--purple)}
.c-green{color:var(--green)}
.c-pink{color:var(--pink)}
.tagline{left:92px;top:306px;width:468px;height:40px;background:var(--purple);border-radius:8px 0 0 8px;color:var(--paper);font-size:22px;padding:10px 0 0 20px}
.date{left:18px;top:359px;font-size:16px}
.rain{left:80px;top:381px;font-size:16px}
.label{font-size:16px;color:var(--pink)}
.loc-label{left:21px;top:405px}
.address{left:17px;top:427px;font-size:13px;font-weight:700;line-height:15px;white-space:normal;width:195px}
.time-label{left:238px;top:412px}
.time{left:231px;top:434px;font-size:20px;color:var(--green)}
.support{left:350px;top:374px;width:88px;text-align:center;font-size:16px;line-height:19px;color:var(--pink)}
.partner{left:440px;top:392px;width:110px;text-align:center;white-space:normal;font-family:var(--body);font-weight:700;font-size:12px;line-height:15px;color:var(--ink);display:flex;flex-direction:column;align-items:center;gap:6px}
.partner-mark{width:12px;height:12px;background:var(--ink)}
.contact{top:488px;font-size:13px;line-height:15px}
.contact-1{left:20px}
.contact-2{left:150px}
.contact .name{font-weight:700}
.contact .org{font-size:9.5px;margin-top:1px}
.contact .phone{font-size:9.5px;margin-top:8px}
.contact .email{font-size:9px;line-height:10px;margin-top:8px;white-space:normal;word-break:break-all}
.contact-1 .email{width:104px}
.contact-2 .email{width:140px;margin-left:-20px}
.events-label{left:18px;top:614px;font-size:17px;color:var(--paper);font-weight:700}
.events-list{left:90px;top:592px;width:140px;font-size:13px;font-weight:700;line-height:15px;text-align:center;white-space:normal}
.events-list li{list-style:none}
.events-list .wash{margin-bottom:7px}
.events-list .pair{display:flex;justify-content:center;gap:18px;margin:3px 0 9px -30px}
.events-list .raffle{margin-bottom:9px;margin-left:-10px}
.events-list .adopt{margin-left:-22px;white-space:nowrap}
.donate{left:37px;top:732px;font-size:14px;font-weight:700;line-height:16px;color:var(--paper)}
</style>
</head>
<body>
<div class="canvas">
  <div class="flyer">
    <svg class="shapes" width="560" height="776" viewBox="0 0 560 776">
      <polygon points="0,14 250,66 250,148 0,176" fill="var(--green)"/>
      <path d="M0,262 Q250,140 560,152 L560,776 L0,776Z" fill="var(--pink)"/>
      <path d="M0,270 Q260,155 560,168 L560,776 L0,776Z" fill="var(--green)"/>
      <path d="M0,276 Q270,170 560,184 L560,776 L0,776Z" fill="var(--purple)"/>
      <path d="M0,330 C120,250 230,212 350,213 Q470,216 560,254 L560,776 L0,776Z" fill="var(--paper)"/>
      <polygon points="72,585 219,585 243,624 250,717 0,717 0,673 40,695 95,635" fill="var(--green)"/>
      <polygon points="0,575 62,569 95,635 40,695 0,673" fill="var(--purple)"/>
      <rect x="0" y="717" width="360" height="59" fill="var(--purple)"/>
      <ellipse cx="325" cy="556" rx="46" ry="56" fill="#8a7560" stroke="var(--purple)" stroke-width="4" role="img" aria-label="Photo of a German shepherd being washed"/>
      <ellipse cx="415" cy="503" rx="45" ry="57" fill="#b89a80" stroke="var(--green)" stroke-width="4" role="img" aria-label="Photo of a volunteer hugging a small spaniel"/>
      <ellipse cx="514" cy="566" rx="46" ry="60" fill="#9aa0a8" stroke="var(--purple)" stroke-width="4" role="img" aria-label="Photo of volunteers drying a puppy in a towel"/>
      <ellipse cx="277" cy="664" rx="48" ry="55" fill="#c8ad8a" stroke="var(--paper)" stroke-width="4" role="img" aria-label="Photo of a tan dog getting a bath"/>
      <path d="M330,776 C345,720 345,660 390,640 C420,630 440,650 470,660 C500,670 540,655 560,668 L560,776Z" fill="#6f8a5a" stroke="var(--pink)" stroke-width="4" role="img" aria-label="Group photo of event volunteers with a mascot"/>
    </svg>

    <div class="txt display annual">3RD<br>ANNUAL</div>
    <div class="txt brand"><span class="brand-dot"></span><span class="brand-name">Maple &amp; Clover</span></div>

    <div class="txt display title-1"><span class="c-purple">MAPLE</span> <span class="c-pink">&amp;</span> <span class="c-green">CLOVER</span></div>
    <div class="txt display title-2">DOG WASH EXTRAVAGANA</div>
    <div class="txt display tagline">A FAMILY FUN EVENT FOR ALL AGES</div>

    <div class="txt display date"><span class="c-pink">DATE:</span> <span class="c-green">SATURDAY APRIL 25TH</span></div>
    <div class="txt display rain c-purple">RAIN DATE: MAY 2ND</div>
    <div class="txt display label loc-label">LOCATION:</div>
    <div class="txt body address">418 Orchard Lane Ave. Harlow Ridge, FL 32099. Brookside Town</div>
    <div class="txt display label time-label">TIME:</div>
    <div class="txt display time">10AM–1PM</div>

    <div class="txt display support">IN<br>SUPPORT<br>OF</div>
    <div class="txt partner"><span class="partner-mark"></span>Circle of Harlow Ridge Pet Center</div>

    <div class="txt body contact contact-1">
      <div class="name">DANA WHITFIELD</div>
      <div class="org">LINDEN REALTY</div>
      <div class="phone">555.201.4417</div>
      <div class="email">DanaWhitfield@lindenrealtygroup.com</div>
    </div>
    <div class="txt body contact contact-2">
      <div class="name">MEGAN ASHBY</div>
      <div class="org">CHRPC</div>
      <div class="phone">555.608.3321</div>
      <div class="email">Megan-Ashby@mailhub.net</div>
    </div>

    <div class="txt body events-label">Events</div>
    <ul class="txt body events-list">
      <li class="wash">FREE Doggie<br>Wash</li>
      <li>Food &amp; Beverage</li>
      <li class="pair"><span>Vendors</span><span>Prizes</span></li>
      <li class="raffle">Raffle Drawings</li>
      <li class="adopt">Adoptions by CHRPC</li>
    </ul>

    <div class="txt body donate">To Make A donation:<br>www.harlowridgepets.org/give</div>
  </div>
</div>
</body>
</html>
```